Velmora Power

We need a business card for "Velmora power". I have uploaded the logo, the color of the card should be according to the logo "Blackish".
Basically velmora power is a solar company.
Also we would like a sample file in which we can edit the information such names and contact details ourselves
The card would be two sided with following details
1- logo on front and underneath the logo there should be a line saying
"Cleaner . Cheaper . Power"
2-website i.e "www.velmorapower.example"
3- Icons for Facebook and Instagram that tells the clients we are available on both social sites.
4- name of the person with his/her designation underneath and email address
5-contact number
6- 1-800--- number with the extension number

its up to the designer how he/she places the details,but it must look professional

5-contact number

Requirements
Must have
• 1- logo on front and underneath the logo there should be a line saying
• "Cleaner . Cheaper . Power"
• 2-website i.e "www.velmorapower.example"
• 3- Icons for Facebook and Instagram that tells the clients we are available on both social sites.
• 4- name of the person with his/her designation underneath and email address
• 5-contact number of the person
• 6- 1-800--- number with the extension number
• 7-card should be in black shade like the logo

```html
<!DOCTYPE html>
<html lang="en">
<head>
<meta charset="utf-8">
<title>Velmora Power – Business Card</title>
<link href="https://fonts.googleapis.com/css2?family=Saira:wght@400;600&family=Roboto:wght@400;500;700&display=swap" rel="stylesheet">
<style>
  :root {
    --page: #e9e9e9;
    --card-core: #0b3147;
    --card-edge: #020609;
    --brand-green: #3cb54a;
    --band-green: #548b4f;
    --name-grey: #c9cccd;
    --ink-dark: #1a1f1c;
    --icon-green: #3f6a3b;
    --white: #ffffff;
    --mark-faint: #0f3442;
  }
  * { margin: 0; padding: 0; box-sizing: border-box; }
  html, body {
    width: 1200px; height: 998px; overflow: hidden;
    background: var(--page);
  }
  .stage { position: relative; width: 1200px; height: 998px; }
  .card {
    position: absolute;
    background: radial-gradient(ellipse at 50% 35%, var(--card-core) 0%, #06151e 55%, var(--card-edge) 100%);
    overflow: hidden;
  }
  .card--front { left: 271px; top: 219px; width: 294px; height: 528px;
    background: radial-gradient(ellipse at 45% 30%, var(--card-core) 0%, #06151e 55%, var(--card-edge) 100%); }
  .card--back { left: 616px; top: 217px; width: 290px; height: 522px; }

  .brand {
    position: absolute; left: 0; right: 0; top: 252px;
    display: flex; align-items: center; justify-content: center; gap: 9px;
  }
  .brand__dot { width: 14px; height: 14px; border-radius: 50%; background: var(--brand-green); }
  .brand__name {
    font-family: "Saira", sans-serif; font-weight: 600; font-size: 26px;
    color: var(--brand-green); line-height: 1;
  }
  .tagline {
    position: absolute; left: 0; right: 0; top: 322px; text-align: center;
    font-family: "Roboto", sans-serif; font-weight: 500; font-size: 9px;
    letter-spacing: 3.4px; color: var(--white);
  }

  .mark-faint {
    position: absolute; left: 0; right: 0; top: 88px; text-align: center;
    font-family: "Saira", sans-serif; font-weight: 600; font-size: 24px;
    color: var(--mark-faint); line-height: 1;
  }
  .person {
    position: absolute; left: 64px; top: 176px;
  }
  .person__name {
    font-family: "Saira", sans-serif; font-weight: 600; font-size: 35px;
    color: var(--name-grey); line-height: 1; letter-spacing: 0.5px;
  }
  .person__role {
    margin-top: 5px;
    font-family: "Roboto", sans-serif; font-size: 10px;
    color: var(--brand-green); letter-spacing: 0.3px;
  }
  .contact-band {
    position: absolute; left: 0; top: 260px; width: 290px; height: 144px;
    background: var(--band-green);
    padding: 21px 0 0 67px;
    list-style: none;
  }
  .contact-band li {
    display: flex; align-items: center; gap: 6px;
    font-family: "Roboto", sans-serif; font-weight: 700; font-size: 13px;
    color: var(--ink-dark); height: 21px;
  }
  .contact-band li.small { font-size: 12px; }
  .contact-band svg { width: 11px; height: 11px; flex: none; }
  .website {
    position: absolute; left: 0; right: 0; top: 449px; text-align: center;
    font-family: "Roboto", sans-serif; font-size: 10.5px;
    letter-spacing: 2.1px; color: var(--brand-green);
  }
</style>
</head>
<body>
<main class="stage">
  <section class="card card--front" aria-label="Card front">
    <div class="brand">
      <span class="brand__dot"></span>
      <span class="brand__name">Velmora Power</span>
    </div>
    <p class="tagline">CLEANER CHEAPER POWER</p>
  </section>

  <section class="card card--back" aria-label="Card back">
    <div class="mark-faint" aria-hidden="true">Velmora Power</div>
    <div class="person">
      <h1 class="person__name">Aren Castell</h1>
      <p class="person__role">FOUNDER / GENERAL MANAGER</p>
    </div>
    <ul class="contact-band">
      <li>
        <svg viewBox="0 0 12 12"><circle cx="6" cy="6" r="6" fill="var(--icon-green)"/><path d="M4 3.2l1.1 1.4-.6.7c.4.9 1 1.5 1.9 1.9l.7-.6L8.5 7.7 7.8 8.8C5.6 8.5 3.5 6.4 3.2 4.2z" fill="var(--band-green)"/></svg>
        001-555-0142
      </li>
      <li>
        <svg viewBox="0 0 12 12"><circle cx="6" cy="6" r="6" fill="var(--icon-green)"/><path d="M4 3.2l1.1 1.4-.6.7c.4.9 1 1.5 1.9 1.9l.7-.6L8.5 7.7 7.8 8.8C5.6 8.5 3.5 6.4 3.2 4.2z" fill="var(--band-green)"/></svg>
        1-800-555-0199
      </li>
      <li class="small">
        <svg viewBox="0 0 12 12"><circle cx="6" cy="6" r="6" fill="var(--icon-green)"/><rect x="3" y="4" width="6" height="4.2" fill="var(--band-green)"/><path d="M3 4l3 2.3L9 4" stroke="var(--icon-green)" stroke-width=".8" fill="none"/></svg>
        aren@velmorapower.example
      </li>
      <li class="small">
        <svg viewBox="0 0 12 12"><circle cx="6" cy="6" r="6" fill="var(--icon-green)"/></svg>
        Aren_castell
      </li>
      <li class="small">
        <svg viewBox="0 0 12 12"><circle cx="6" cy="6" r="6" fill="var(--icon-green)"/></svg>
        Aren_castell
      </li>
    </ul>
    <p class="website">www.velmorapower.example</p>
  </section>
</main>
</body>
</html>
```